Flyer-Design für Kreativwerkstatt
Zielgruppe
Kreativwerkstatt für Touristen - vorrangig Frauen
Aufgabenstellung
1 mal gefaltet
Wenn möglich außer dem Logo noch folgenden Text verwenden
Kreativität fängt da ,wo der Verstand aufhört das denken zu behindern

```html
<!DOCTYPE html>
<html lang="de">
<head>
<meta charset="utf-8">
<title>Papierhandwerk erlernen – Flyer</title>
<link href="https://fonts.googleapis.com/css2?family=Lexend:wght@300;400;500&display=swap" rel="stylesheet">
<style>
  :root {
    --cream: #fdf0c8;
    --orange: #e2731d;
    --paper-light: #e9e1cf;
    --paper-mid: #cfc3a5;
    --gap: #ffffff;
  }
  * { margin: 0; padding: 0; box-sizing: border-box; }
  html, body { width: 1200px; height: 595px; overflow: hidden; background: var(--gap); }
  body { font-family: "Lexend", sans-serif; color: var(--orange); position: relative; }
  .panel { position: absolute; left: 0; width: 1200px; background: var(--cream); }
  .panel--outside { top: 5px; height: 284px; }
  .panel--inside { top: 304px; height: 284px; }
  .abs { position: absolute; }

  .kicker { left: 31px; top: 30px; font-size: 12.5px; font-weight: 400; }
  .headline { font-size: 23px; font-weight: 400; line-height: 1; white-space: nowrap; }
  .headline--a { left: 46px; top: 47px; }
  .headline--b { left: 93px; top: 71px; }
  .engraving { left: 389px; top: 12px; width: 156px; height: 92px; border-radius: 4px;
    background: linear-gradient(160deg, #f2e6c4, #b9ad92 60%, #e9dcb8); }

  .course { top: 123px; width: 150px; font-size: 8.3px; line-height: 9.7px; font-weight: 300; }
  .course h3 { font-size: 8.8px; font-weight: 500; line-height: 10px; }
  .course--1 { left: 42px; } .course--2 { left: 231px; } .course--3 { left: 419px; }
  .price { top: 188px; font-size: 11px; font-weight: 400; text-align: right; width: 80px; }
  .price--1 { left: 125px; } .price--2 { left: 316px; } .price--3 { left: 500px; }

  .contact { top: 230px; font-size: 6.9px; line-height: 7.5px; font-weight: 300; }
  .contact--address { left: 59px; }
  .contact--web { left: 149px; }
  .icon { position: absolute; }
  .cta { left: 290px; top: 231px; font-size: 16.5px; font-weight: 400; }
  .cta-sub { left: 301px; top: 256px; font-size: 9px; font-weight: 400; }

  .handmade-paper { left: 598px; top: 58px; width: 330px; height: 233px; z-index: 1; }
  .title-right { left: 622px; top: 24px; font-size: 31px; line-height: 31px; font-weight: 400; z-index: 2; }
  .brand { right: 30px; font-size: 26px; font-weight: 400; display: flex; align-items: center; gap: 8px; }
  .brand-dot { width: 12px; height: 12px; border-radius: 50%; background: var(--orange); }
  .panel--outside .brand { top: 56px; }
  .panel--inside .brand { top: 52px; }
  .quote { left: 952px; top: 231px; font-size: 12px; line-height: 12.5px; font-weight: 300; letter-spacing: 0.4px; white-space: nowrap; }
  .quote span { display: block; }

  .section-title { left: 42px; top: 20px; font-size: 30px; font-weight: 400; letter-spacing: 0.5px; }
  .section-sub { left: 181px; top: 52px; font-size: 17px; font-weight: 400; }
  .craft { top: 95px; width: 152px; }
  .craft h3 { font-size: 9.5px; font-weight: 400; letter-spacing: 1.2px; margin-bottom: 5px; }
  .craft .photo { width: 150px; height: 73px; }
  .craft p { margin-top: 12px; font-size: 8.5px; line-height: 9.6px; font-weight: 300; letter-spacing: 0.4px; }
  .craft--1 { left: 41px; } .craft--2 { left: 234px; } .craft--3 { left: 425px; }
  .photo--scoop { background: linear-gradient(135deg, #9fae84, #c7a783 55%, #8a6d4a); }
  .photo--bind { background: linear-gradient(135deg, #3a2b22, #c9a574 55%, #6e4b2d); }
  .photo--box { background: linear-gradient(135deg, #f2f2f4, #3a3a3d 50%, #f4f4f6); }

  .workshop { left: 630px; top: 65px; width: 232px; height: 149px;
    background: linear-gradient(160deg, #e8e4d8, #5c5a52 45%, #b8a27c); }
  .portrait { left: 831px; top: 37px; width: 63px; height: 80px;
    background: linear-gradient(180deg, #d7d2c8, #2e2a2a 70%, #d9c4a2); }
  .about { left: 877px; top: 131px; width: 240px; }
  .about h3 { font-size: 9.5px; font-weight: 400; letter-spacing: 1.2px; margin-bottom: 8px; }
  .about p { font-size: 8.3px; line-height: 9.6px; font-weight: 300; text-align: justify; letter-spacing: 0.3px; }
  .tagline { left: 0; width: 1200px; top: 255px; text-align: center; font-size: 16px; letter-spacing: 2px; font-weight: 400; }
</style>
</head>
<body>

<section class="panel panel--outside">
  <p class="abs kicker">Altes Handwerk neu belebt</p>
  <h1 class="abs headline headline--a">eine besondere Auszeit -</h1>
  <p class="abs headline headline--b">Papierhandwerk erlernen</p>
  <div class="abs engraving" role="img" aria-label="Historischer Stich: Papiermacher schöpft Papier an der Bütte"></div>

  <div class="abs course course--1"><h3>SCHNUPPERKURS</h3>Interessierte, die sich gerne mit dem Werkstoff Papier beschäf­tigen, erlernen unter fachkun­diger Anleitung die Grundlagen des Buchbinderhandwerks ......</div>
  <div class="abs course course--2"><h3>EINSTIEGERKURS</h3>Interessierte, die sich gerne mit dem Werkstoff Papier beschäf­tigen, erlernen unter fachkun­diger Anleitung die Grundlagen des Buchbinderhandwerks ......</div>
  <div class="abs course course--3"><h3>FORTGESCHRITTENENKURS</h3>Interessierte, die sich gerne mit dem Werkstoff Papier beschäf­tigen, erlernen unter fachkun­diger Anleitung die Grundlagen des Buchbinderhandwerks ......</div>
  <p class="abs price price--1">€ 80,-</p>
  <p class="abs price price--2">€ 120,-</p>
  <p class="abs price price--3">€ 220,-</p>

  <svg class="icon" style="left:42px;top:231px" width="11" height="15" viewBox="0 0 11 15" aria-hidden="true">
    <path d="M5.5 0.5a4.8 4.8 0 0 1 4.8 4.8c0 3.4-4.8 8.2-4.8 8.2S0.7 8.7 0.7 5.3A4.8 4.8 0 0 1 5.5 0.5z" fill="var(--orange)"/>
    <circle cx="5.5" cy="5.2" r="1.8" fill="var(--cream)"/>
    <ellipse cx="5.5" cy="14" rx="4" ry="0.8" fill="none" stroke="var(--orange)" stroke-width="0.6"/>
  </svg>
  <p class="abs contact contact--address">Kreativwerkstatt<br>Bastelhaus<br>Lindenweg 12<br>12345 MUSTERSTADT</p>
  <svg class="icon" style="left:134px;top:231px" width="12" height="12" viewBox="0 0 12 12" aria-hidden="true">
    <circle cx="6" cy="6" r="2.2" fill="none" stroke="var(--orange)" stroke-width="1.2"/>
    <path d="M8.2 4v2.8c0 1.4 2.6 1.4 2.6-0.8A4.8 4.8 0 1 0 8.5 10" fill="none" stroke="var(--orange)" stroke-width="1.2"/>
  </svg>
  <svg class="icon" style="left:135px;top:245px" width="11" height="11" viewBox="0 0 11 11" aria-hidden="true">
    <path d="M2.2 1l2 2.2-1 1.3a6 6 0 0 0 3.3 3.3l1.3-1 2.2 2-1.2 1.7C4.8 10.5 0.5 6.2 0.5 2.2z" fill="none" stroke="var(--orange)" stroke-width="1"/>
  </svg>
  <p class="abs contact contact--web">bastelhaus-werkstatt.de<br>kreativwerkstatt@bastelhaus<br>0176 000000000</p>

  <p class="abs cta">jetzt anmelden</p>
  <p class="abs cta-sub">und eine besondere Auszeit erleben</p>

  <svg class="abs handmade-paper" viewBox="0 0 330 233" role="img" aria-label="Handgeschöpftes Papier mit eingearbeiteten Blüten">
    <defs>
      <linearGradient id="paperTone" x1="0" y1="0" x2="1" y2="1">
        <stop offset="0" stop-color="var(--paper-light)"/>
        <stop offset="1" stop-color="var(--paper-mid)"/>
      </linearGradient>
    </defs>
    <path d="M180 8 L200 2 L235 15 L250 45 L262 80 L290 105 L300 135 L318 140 L322 155 L300 175 L310 205 L290 233 L0 233 L0 105 L40 95 L75 68 L110 52 L150 38 Z" fill="url(#paperTone)"/>
  </svg>
  <h2 class="abs title-right">PAPIERHANDWERK<br>erlernen</h2>

  <div class="abs brand"><span class="brand-dot"></span>Bastelhaus</div>

  <p class="abs quote">
    <span>Kreativität fängt da an,</span>
    <span style="padding-left:16px">wo der Verstand aufhört</span>
    <span style="padding-left:37px">das Denken zu behindern</span>
  </p>
</section>

<section class="panel panel--inside">
  <h2 class="abs section-title">WERKSTOFF PAPIER</h2>
  <p class="abs section-sub">Altes Handwerk - moderne Materialien</p>

  <div class="abs craft craft--1">
    <h3>PAPIERSCHÖPFEN</h3>
    <div class="photo photo--scoop" role="img" aria-label="Hände schöpfen Papier aus der Bütte"></div>
    <p>Lerne Dein eigenes<br>besonderes<br>Papier herzustellen</p>
  </div>
  <div class="abs craft craft--2">
    <h3>BUCHBINDEN</h3>
    <div class="photo photo--bind" role="img" aria-label="Hände heften einen Buchblock"></div>
    <p>Gestalte Dein eigenes Buch<br>und setze es durch Leder<br>richtig in Szene.</p>
  </div>
  <div class="abs craft craft--3">
    <h3>KASSETTEN</h3>
    <div class="photo photo--box" role="img" aria-label="Schwarze Kassette mit rotem Innenfutter"></div>
    <p>Kreiere einen<br>„Schuhkarton“<br>als Schatzkiste</p>
  </div>

  <div class="abs workshop" role="img" aria-label="Blick in die Werkstatt mit Arbeitstischen und Pressen"></div>
  <div class="abs portrait" role="img" aria-label="Porträt der Werkstattleiterin bei der Arbeit"></div>

  <div class="abs brand"><span class="brand-dot"></span>Bastelhaus</div>

  <div class="abs about">
    <h3>ÜBER MICH</h3>
    <p>Lorem ipsum dolor sit amet, consetetur sadipscing elitr, sed diam nonumy eirmod tempor invidunt ut labore et dolore magna aliquyam erat, sed diam voluptua. At vero eos et accusam et justo duo dolores et ea rebum. Stet clita kasd gubergren, no sea takimata sanctus est Lorem ipsum dolor sit amet. Lorem ipsum dolor sit amet, consetetur sadipscing elitr, sed diam</p>
  </div>

  <p class="abs tagline">Wir möchten Dich mit traditionellem Handwerk rund um das Papier vertraut machen!</p>
</section>

</body>
</html>
```